Lost Teens Auto Doantion Website Design

Please create a new one page website design.

Current site: http://autosforyouth.net/

New WEBSITE address is: SedansForLostTeens.org

Use these sites for an idea of what I am looking for. I like these sites best: tiresforretirees.org and trucksforelders.org

Coding

Coded - Design and coding required

Number of Pages Required

1 page

```html
<!DOCTYPE html>
<html lang="en">
<head>
<meta charset="utf-8">
<title>Autos For Youth – Help Find Missing Kids</title>
<link href="https://fonts.googleapis.com/css2?family=Oswald:wght@400;500&family=Roboto+Condensed:wght@400;700&family=Open+Sans:wght@400;600&display=swap" rel="stylesheet">
<style>
:root{
  --red:#c3121d;
  --red-dark:#9c0c15;
  --navy:#1b3a8c;
  --navy-deep:#14307a;
  --blue:#1a73d0;
  --ribbon:#1f86e0;
  --white:#ffffff;
  --ink:#2b2b2b;
  --muted:#555c66;
  --line:#c9ced6;
  --foot:#ececec;
}
*{box-sizing:border-box;margin:0;padding:0}
html,body{width:1200px;height:3564px;overflow:hidden}
body{position:relative;background:var(--white);font-family:'Open Sans',sans-serif;color:var(--ink)}
.abs{position:absolute}

/* header */
.site-header{position:absolute;left:0;top:0;width:1200px;height:114px;background:linear-gradient(90deg,var(--red-dark),var(--red) 40%,#b5101b)}
.brand{position:absolute;left:131px;top:24px;color:var(--white)}
.brand-name{font-family:'Oswald',sans-serif;font-weight:500;font-size:34px;line-height:38px}
.brand-tag{font-family:'Oswald',sans-serif;font-size:17px;letter-spacing:.5px;margin-left:20px}
.main-nav{position:absolute;top:42px;left:470px;display:flex;gap:22px;font-family:'Oswald',sans-serif;font-size:15px;color:var(--white);text-transform:uppercase}
.nav-cta{position:absolute;left:962px;top:38px;width:106px;height:38px;background:var(--blue);color:var(--white);font-family:'Oswald',sans-serif;font-size:14px;line-height:38px;text-align:center;text-transform:uppercase}

/* hero */
.hero{position:absolute;left:0;top:114px;width:1200px;height:563px}
.hero-photo{position:absolute;inset:0;background:linear-gradient(100deg,#5a5a52 0%,#8b8470 30%,#b38a3a 55%,#c29c4e 80%,#9b8456 100%)}
.donate-panel{position:absolute;left:684px;top:0;width:383px;height:563px;background:var(--navy)}
.call-line{position:absolute;left:120px;top:32px;color:var(--white);font-family:'Roboto Condensed',sans-serif;font-size:18px;line-height:22px}
.phone-badge{position:absolute;left:72px;top:37px;width:40px;height:40px;border:2px solid var(--white);border-radius:50%}
.ribbon{position:absolute;left:0;top:114px;width:383px;height:82px}
.ribbon-text{position:absolute;left:0;top:128px;width:383px;text-align:center;color:var(--white)}
.ribbon-text h3{font-family:'Oswald',sans-serif;font-weight:400;font-size:19px;text-transform:uppercase}
.ribbon-text p{font-size:10px;margin-top:2px}
.field{position:absolute;height:36px;background:var(--white);border:1px solid var(--line);font-size:10px;color:#6a6f78;padding:11px 9px}
.field.select::after{content:"";position:absolute;right:10px;top:14px;border:4px solid transparent;border-top-color:#444}
.submit{position:absolute;left:117px;top:489px;width:149px;height:38px;background:var(--blue);color:var(--white);font-family:'Oswald',sans-serif;font-size:14px;line-height:38px;text-align:center;text-transform:uppercase}

/* how to donate */
.how{position:absolute;left:0;top:677px;width:1200px;height:530px;background:linear-gradient(180deg,#fff 0%,#f3f4f7 100%)}
.section-title{position:absolute;left:0;width:1200px;top:72px;text-align:center;font-family:'Roboto Condensed',sans-serif;font-weight:400;font-size:34px;color:#1f1f1f;letter-spacing:1px}
.section-title span{color:var(--red)}
.step{position:absolute;top:190px;width:214px;height:214px}
.step-label{position:absolute;left:0;top:122px;width:214px;text-align:center;color:var(--white);font-family:'Oswald',sans-serif;font-size:17px;line-height:22px}

/* benefits band */
.benefits{position:absolute;left:0;top:1207px;width:1200px;height:278px;background:var(--navy-deep)}
.benefit{position:absolute;top:80px;width:150px;text-align:center;color:var(--white)}
.benefit svg{display:block;margin:0 auto}
.benefit p{margin-top:12px;font-family:'Roboto Condensed',sans-serif;font-size:15px;line-height:18px}

/* awareness */
.awareness{position:absolute;left:0;top:1485px;width:1200px;height:779px}
.kids-photo{position:absolute;left:0;top:0;width:582px;height:779px;background:linear-gradient(135deg,#6b4a32 0%,#b6574a 40%,#d23a4f 65%,#5b3a45 100%)}
.awareness-copy{position:absolute;left:642px;top:104px;width:450px}
.awareness-copy h2{font-family:'Roboto Condensed',sans-serif;font-weight:700;font-size:23px;line-height:34px;color:var(--navy);text-transform:uppercase}
.awareness-copy p{font-size:12.5px;line-height:23px;color:var(--ink)}
.stat{position:absolute;display:flex;align-items:center;gap:14px}
.stat-ring{width:72px;height:72px;border:2px solid var(--red);border-radius:50%;display:flex;align-items:center;justify-content:center;font-family:'Roboto Condensed',sans-serif;font-weight:700;font-size:15px;color:var(--red)}
.stat-text{font-size:12.5px;line-height:17px;width:160px}

/* faq */
.faq{position:absolute;left:0;top:2264px;width:1200px;height:675px}
.faq h2{position:absolute;left:74px;top:88px;font-family:'Roboto Condensed',sans-serif;font-weight:700;font-size:38px;color:var(--navy)}
.faq-item{position:absolute;left:67px;width:451px;height:38px;border:1px solid var(--line);border-radius:19px;font-size:12.5px;line-height:36px;padding-left:18px;color:#333}
.faq-item svg{position:absolute;right:16px;top:13px}
.car-photo{position:absolute;left:582px;top:0;width:618px;height:675px;background:linear-gradient(180deg,#d7dade 0%,#b9bdc3 40%,#9a2a2c 55%,#c22b30 65%,#7a7b7d 80%,#5c5d60 100%)}

/* footer */
.site-footer{position:absolute;left:0;top:2939px;width:1200px;height:387px;background:var(--foot)}
.foot-col{position:absolute;top:104px}
.foot-col h4{font-family:'Roboto Condensed',sans-serif;font-weight:700;font-size:20px;color:#222;text-transform:uppercase;margin-bottom:18px}
.foot-col p,.foot-col li{font-size:12px;line-height:18px;color:#333}
.news-input{margin-top:16px;width:320px;height:38px;border:1px solid var(--line);background:var(--white);font-size:11px;color:#666;padding:11px 12px}
.subscribe{margin-top:19px;width:147px;height:36px;background:var(--red);color:var(--white);font-family:'Roboto Condensed',sans-serif;font-weight:700;font-size:13px;line-height:36px;text-align:center;text-transform:uppercase}
.contact-row{display:flex;gap:12px;align-items:flex-start;margin-bottom:14px}
.socials{display:flex;gap:6px;margin-top:18px}
.socials span{width:26px;height:26px;border:1.5px solid #333;border-radius:50%}
.quick-links{list-style:none}
.quick-links li{line-height:24px}

/* legal */
.legal{position:absolute;left:0;top:3326px;width:1200px;height:238px;text-align:center}
.legal h5{margin-top:62px;font-family:'Open Sans',sans-serif;font-weight:400;font-size:15px;color:#222}
.legal .disclaimer{margin:20px auto 0;width:1130px;font-size:11px;line-height:27px;color:#333}
.legal .copyright{margin-top:18px;font-size:11px;color:#333}
</style>
</head>
<body>

<header class="site-header">
  <div class="brand">
    <div class="brand-name">Autos For Youth</div>
    <div class="brand-tag">Help Find Missing Kids</div>
  </div>
  <nav class="main-nav">
    <span>Home</span><span>About Seek The Young</span><span>Missing Kids</span><span>FAQ</span><span>Contact</span>
  </nav>
  <div class="nav-cta">Donate Now</div>
</header>

<section class="hero">
  <div class="hero-photo" role="img" aria-label="Black SUV parked on an autumn road with two young children standing beside it"></div>
  <div class="donate-panel">
    <div class="phone-badge">
      <svg width="36" height="36" viewBox="0 0 36 36"><path d="M12 10c1-1 2-1 3 0l2 3c.6 1 .3 1.8-.5 2.5l-1 .8c1 2.3 2.7 4 5 5l.8-1c.7-.8 1.5-1.1 2.5-.5l3 2c1 1 1 2 0 3l-1.4 1.4c-1.6 1.6-5 .5-8.6-3.1S9 15 10.6 13.4z" fill="#fff"/></svg>
    </div>
    <div class="call-line">CALL TODAY TO DONATE<br>1-800-555-0142</div>
    <svg class="ribbon" viewBox="0 0 383 82" preserveAspectRatio="none"><path d="M0 20 Q191 -8 383 20 L383 68 Q191 96 0 68 Z" fill="var(--ribbon)"/></svg>
    <div class="ribbon-text">
      <h3>2-Step Donation - Made Quick &amp; Easy</h3>
      <p>Fill out the form &amp; help protect the future of children.</p>
    </div>
    <div class="field" style="left:22px;top:247px;width:164px">FirstName</div>
    <div class="field" style="left:198px;top:247px;width:163px">LastName</div>
    <div class="field" style="left:22px;top:295px;width:164px">ZIPCode</div>
    <div class="field" style="left:198px;top:295px;width:163px">Daytime Phone</div>
    <div class="field" style="left:22px;top:342px;width:339px">Email</div>
    <div class="field select" style="left:22px;top:394px;width:164px">Choose Year</div>
    <div class="field select" style="left:198px;top:394px;width:163px">Choose Make</div>
    <div class="field" style="left:22px;top:442px;width:339px">Vehicle Model</div>
    <div class="submit">Donate Now</div>
  </div>
</section>

<section class="how">
  <h2 class="section-title">HOW TO <span>DONATE</span></h2>

  <div class="step" style="left:164px">
    <svg width="214" height="214" viewBox="0 0 214 214"><circle cx="107" cy="107" r="103" fill="none" stroke="var(--navy)" stroke-width="2" stroke-dasharray="5 4"/><circle cx="107" cy="107" r="92" fill="var(--navy)"/>
      <g fill="#fff"><rect x="82" y="58" width="34" height="20" rx="2"/><rect x="116" y="64" width="16" height="14" rx="2"/><path d="M120 44 L100 58" stroke="#fff" stroke-width="4"/><circle cx="93" cy="82" r="6"/><circle cx="124" cy="82" r="6"/></g></svg>
    <div class="step-label">Fast Free Pickup<br>24hr Response</div>
  </div>
  <svg class="abs" style="left:396px;top:290px" width="80" height="14"><path d="M2 7 H70" stroke="#222" stroke-width="2" stroke-dasharray="5 4"/><path d="M68 2 L76 7 L68 12" fill="none" stroke="#222" stroke-width="2"/></svg>

  <div class="step" style="left:492px">
    <svg width="214" height="214" viewBox="0 0 214 214"><circle cx="107" cy="107" r="103" fill="none" stroke="var(--red)" stroke-width="2" stroke-dasharray="5 4"/><circle cx="107" cy="107" r="92" fill="var(--red)"/>
      <rect x="90" y="40" width="34" height="44" rx="2" fill="none" stroke="#fff" stroke-width="3"/><path d="M96 52 H118 M96 60 H118 M96 68 H110" stroke="#fff" stroke-width="2"/></svg>
    <div class="step-label">Tax Deduction<br>Easy To Do!</div>
  </div>
  <svg class="abs" style="left:724px;top:290px" width="80" height="14"><path d="M2 7 H70" stroke="#222" stroke-width="2" stroke-dasharray="5 4"/><path d="M68 2 L76 7 L68 12" fill="none" stroke="#222" stroke-width="2"/></svg>

  <div class="step" style="left:817px">
    <svg width="214" height="214" viewBox="0 0 214 214"><circle cx="107" cy="107" r="103" fill="none" stroke="var(--navy)" stroke-width="2" stroke-dasharray="5 4"/><circle cx="107" cy="107" r="92" fill="var(--navy)"/>
      <rect x="90" y="42" width="30" height="40" rx="2" fill="none" stroke="#fff" stroke-width="3"/><path d="M96 54 H114 M96 62 H114 M96 70 H108" stroke="#fff" stroke-width="2"/><path d="M112 80 L128 56" stroke="#fff" stroke-width="4"/></svg>
    <div class="step-label">No Emission<br>Test Required</div>
  </div>
</section>

<section class="benefits">
  <div class="benefit" style="left:122px">
    <svg width="64" height="64" viewBox="0 0 64 64"><circle cx="32" cy="32" r="30" fill="none" stroke="#fff" stroke-width="2"/><rect x="20" y="20" width="24" height="24" rx="3" fill="none" stroke="#fff" stroke-width="2.5"/><path d="M25 32 L30 37 L41 25" fill="none" stroke="#fff" stroke-width="3"/></svg>
    <p>You have no<br>costs</p>
  </div>
  <div class="benefit" style="left:277px">
    <svg width="64" height="64" viewBox="0 0 64 64"><circle cx="32" cy="32" r="30" fill="none" stroke="#fff" stroke-width="2"/><rect x="18" y="30" width="18" height="10" fill="#fff"/><rect x="36" y="33" width="10" height="7" fill="#fff"/><path d="M40 22 L30 30" stroke="#fff" stroke-width="2.5"/><circle cx="24" cy="43" r="3.5" fill="#fff"/><circle cx="41" cy="43" r="3.5" fill="#fff"/></svg>
    <p>Free towing,<br>running or not</p>
  </div>
  <div class="benefit" style="left:438px">
    <svg width="64" height="64" viewBox="0 0 64 64"><circle cx="32" cy="32" r="30" fill="none" stroke="#fff" stroke-width="2"/><rect x="22" y="17" width="20" height="30" rx="2" fill="none" stroke="#fff" stroke-width="2.5"/><path d="M26 25 H38 M26 31 H38 M26 37 H34" stroke="#fff" stroke-width="2"/></svg>
    <p>We issue you an<br>IRS tax receipt</p>
  </div>
  <div class="benefit" style="left:595px">
    <svg width="64" height="64" viewBox="0 0 64 64"><circle cx="32" cy="32" r="30" fill="none" stroke="#fff" stroke-width="2"/><rect x="21" y="18" width="18" height="26" rx="2" fill="none" stroke="#fff" stroke-width="2.5"/><circle cx="38" cy="38" r="6" fill="none" stroke="#fff" stroke-width="2.5"/><path d="M42 42 L47 47" stroke="#fff" stroke-width="2.5"/></svg>
    <p>We take care of<br>all paperwork</p>
  </div>
  <div class="benefit" style="left:749px">
    <svg width="64" height="64" viewBox="0 0 64 64"><circle cx="32" cy="32" r="30" fill="none" stroke="#fff" stroke-width="2"/><rect x="21" y="18" width="22" height="28" rx="2" fill="none" stroke="#fff" stroke-width="2.5"/><rect x="27" y="15" width="10" height="6" fill="#fff"/><path d="M26 30 H38 M26 36 H38" stroke="#fff" stroke-width="2"/></svg>
    <p>No DMV Hassles</p>
  </div>
  <div class="benefit" style="left:909px">
    <svg width="64" height="64" viewBox="0 0 64 64"><circle cx="32" cy="32" r="30" fill="none" stroke="#fff" stroke-width="2"/><rect x="19" y="24" width="26" height="20" rx="3" fill="none" stroke="#fff" stroke-width="2.5"/><path d="M27 24 V19 H37 V24" fill="none" stroke="#fff" stroke-width="2.5"/><path d="M19 32 H45" stroke="#fff" stroke-width="2"/></svg>
    <p>Vacation Voucher</p>
  </div>
</section>

<section class="awareness">
  <div class="kids-photo" role="img" aria-label="Two smiling young girls in bright traditional clothing sitting together"></div>
  <svg class="abs" style="left:582px;top:0" width="40" height="40"><polygon points="0,0 40,0 0,40" fill="var(--navy-deep)"/></svg>
  <div class="awareness-copy">
    <h2>Every 10 minutes, there's an attempt to abduct a child. Most parents don't think it will happen to them.</h2>
    <p style="margin-top:28px">According to the Department of Justice, each year, there are approximately 94,000 missing children, 90,000 runaways, 300 stranger abductions, and 981 family abductions.</p>
  </div>
  <div class="stat" style="left:646px;top:346px"><div class="stat-ring">800,000</div><div class="stat-text">Children are reported missing a year</div></div>
  <div class="stat" style="left:910px;top:375px"><div class="stat-ring">400+</div><div class="stat-text" style="width:110px">Open missing children cases</div></div>
  <div class="stat" style="left:646px;top:432px"><div class="stat-ring">751,000</div><div class="stat-text">Children have seen the Seek The Young program</div></div>
  <p class="abs" style="left:650px;top:530px;width:440px;font-size:12.5px;line-height:23px">You can help protect the future of children by supporting Seek The Young through your car donation. Your donated vehicle or vessel will be sold at auction and the net proceeds will be returned to Seek The Young.</p>
</section>

<section class="faq">
  <h2>FAQ</h2>
  <div class="faq-item" style="top:183px">Why donate a vehicle or vessel?<svg width="12" height="8"><path d="M1 1 L6 6 L11 1" fill="none" stroke="#222" stroke-width="2"/></svg></div>
  <div class="faq-item" style="top:231px">How do I donate a vehicle or vessel?<svg width="12" height="8"><path d="M1 1 L6 6 L11 1" fill="none" stroke="#222" stroke-width="2"/></svg></div>
  <div class="faq-item" style="top:279px">How does my vehicle or vessel donation benefit the charity?<svg width="12" height="8"><path d="M1 1 L6 6 L11 1" fill="none" stroke="#222" stroke-width="2"/></svg></div>
  <div class="faq-item" style="top:327px">How does donating a car or boat benefit my taxes?<svg width="12" height="8"><path d="M1 1 L6 6 L11 1" fill="none" stroke="#222" stroke-width="2"/></svg></div>
  <div class="faq-item" style="top:375px">How long does it take to pickup my donation?<svg width="12" height="8"><path d="M1 1 L6 6 L11 1" fill="none" stroke="#222" stroke-width="2"/></svg></div>
  <div class="faq-item" style="top:423px">What happens to my car after it's picked up?<svg width="12" height="8"><path d="M1 1 L6 6 L11 1" fill="none" stroke="#222" stroke-width="2"/></svg></div>
  <div class="faq-item" style="top:471px">Do I have any liability after the vehicle/vessel is picked up?<svg width="12" height="8"><path d="M1 1 L6 6 L11 1" fill="none" stroke="#222" stroke-width="2"/></svg></div>
  <div class="faq-item" style="top:519px">What kinds of donations can the charity accept?<svg width="12" height="8"><path d="M1 1 L6 6 L11 1" fill="none" stroke="#222" stroke-width="2"/></svg></div>
  <div class="car-photo" role="img" aria-label="Red hatchback car driving on an open road"></div>
</section>

<footer class="site-footer">
  <div class="foot-col" style="left:131px;width:330px">
    <h4>Sign up for newsletter</h4>
    <p>Excepteur sint occaecat cupidatat non proident, sunt in culpa qui officia deserunt</p>
    <div class="news-input">Enter email</div>
    <div class="subscribe">Subscribe</div>
  </div>
  <div class="foot-col" style="left:546px;width:260px">
    <h4>Contact us</h4>
    <div class="contact-row">
      <svg width="12" height="16" viewBox="0 0 12 16"><path d="M6 0a6 6 0 0 0-6 6c0 4.5 6 10 6 10s6-5.5 6-10a6 6 0 0 0-6-6z" fill="var(--red)"/><circle cx="6" cy="6" r="2.2" fill="#fff"/></svg>
      <p>Autos For Youth<br>118 Maple Ave., Suite 210-B, Fairview NJ 08000</p>
    </div>
    <div class="contact-row">
      <svg width="12" height="14" viewBox="0 0 36 36"><path d="M8 4c2-2 4-2 5 0l3 5c1 2 .5 3-1 4l-2 2c2 4 5 7 9 9l2-2c1-1.5 2-2 4-1l5 3c2 1 2 3 0 5l-2 2c-3 3-9 1-16-6S5 7 8 4z" fill="var(--red)"/></svg>
      <p>Phone:&nbsp; 888-555-0197</p>
    </div>
    <div class="contact-row">
      <svg width="13" height="12" viewBox="0 0 13 12"><rect x="0" y="1" width="13" height="10" fill="var(--red)"/><path d="M0 1 L6.5 7 L13 1" fill="none" stroke="#fff" stroke-width="1.3"/></svg>
      <p>Email: info@autosforyouth.net</p>
    </div>
    <div class="socials"><span></span><span></span><span></span><span></span></div>
  </div>
  <div class="foot-col" style="left:851px;width:200px">
    <h4>Quick links</h4>
    <ul class="quick-links">
      <li>Home</li><li>About Seek The Young</li><li>Missing Kids</li><li>Contact</li><li>Faq</li>
    </ul>
  </div>
</footer>

<section class="legal">
  <h5>Privacy Policy</h5>
  <p class="disclaimer">www.autosforyouth.net is not affiliated with Rides4Youth, RidesForYouth, WheelsForKids, Wheels4Kids, National Motor Aid For Kids, or any other website. Your donation to www.autosforyouth.net will benefit Seek The Young, a registered Non Profit organization that helps find missing children. Seek The Young is not affiliated with wheels for kids, wheelsforkids, rides 4 youth, rides for youth.</p>
  <p class="copyright">© Autos For Youth 2018, All Rights Reserved</p>
</section>

</body>
</html>
```